Talvex Industrial Maintenance Business Card

Design a business card with the following information, logo must be included.
Talvex Industrial Maintenance
Dale Virnow Jr.
Pone 413-627-8154
email dale.virnow.jr@brindlemail.net

```html
<!DOCTYPE html>
<html lang="en">
<head>
<meta charset="utf-8">
<title>Talvex Industrial Maintenance – Business Card</title>
<link rel="stylesheet" href="https://fonts.googleapis.com/css2?family=Archivo+Black&family=Montserrat:wght@500;600;700&display=swap">
<style>
  :root {
    --page-bg: #e9eaeb;
    --card-black: #0d0d0d;
    --brand-blue: #1b73c4;
    --photo-deep: #0f2f52;
    --photo-mid: #2a6296;
    --photo-light: #8fb8de;
    --white: #ffffff;
    --ink: #2b2b2b;
    --muted: #8a8a8a;
  }
  * { box-sizing: border-box; margin: 0; padding: 0; }
  html, body { width: 1200px; height: 900px; overflow: hidden; }
  body {
    background: var(--page-bg);
    font-family: "Montserrat", Arial, sans-serif;
    display: flex;
    align-items: center;
    justify-content: center;
    gap: 24px;
  }
  .card {
    position: relative;
    width: 560px;
    height: 320px;
    overflow: hidden;
    background: var(--card-black);
    box-shadow: 0 14px 30px rgba(0,0,0,0.22);
  }

  /* Front */
  .card-front { display: flex; align-items: center; justify-content: center; }
  .brand-lockup { display: flex; align-items: center; gap: 16px; }
  .brand-dot {
    width: 58px; height: 58px; border-radius: 50%;
    background: var(--brand-blue);
  }
  .brand-name {
    color: var(--brand-blue);
    font-weight: 600;
    line-height: 1.05;
  }
  .brand-name .line-main { display: block; font-size: 56px; letter-spacing: 1px; }
  .brand-name .line-sub { display: block; font-size: 14.5px; letter-spacing: 1.2px; }

  /* Back */
  .card-back .backdrop { position: absolute; inset: 0; }
  .identity { position: absolute; left: 34px; top: 26px; }
  .identity .first-name,
  .identity .last-name {
    font-family: "Archivo Black", Arial, sans-serif;
    font-size: 30px; line-height: 1.0; letter-spacing: 2px;
  }
  .identity .first-name { color: var(--white); }
  .identity .last-name { color: var(--brand-blue); }
  .identity .role {
    margin-top: 6px;
    color: var(--white); font-weight: 500; font-size: 15px; letter-spacing: 0.5px;
  }
  .identity .rule {
    margin-top: 14px; width: 170px; height: 3px; background: var(--white);
  }
  .contacts { position: absolute; left: 30px; top: 172px; display: flex; flex-direction: column; gap: 12px; }
  .contact-pill {
    display: flex; align-items: center; gap: 10px;
    background: var(--white); border-radius: 18px;
    height: 34px; padding: 0 18px 0 6px;
    color: var(--ink); font-weight: 600;
  }
  .contact-pill.phone { font-size: 19px; font-weight: 700; width: 260px; }
  .contact-pill.email { font-size: 13px; width: 300px; }
  .contact-icon {
    width: 24px; height: 24px; border-radius: 50%;
    background: #4a4a4a; display: flex; align-items: center; justify-content: center;
    flex: none;
  }
  .corner-brand {
    position: absolute; right: 28px; bottom: 28px;
    display: flex; align-items: center; gap: 8px;
  }
  .corner-brand .brand-dot { width: 34px; height: 34px; }
  .corner-brand .brand-name { font-size: 20px; letter-spacing: 1px; }
</style>
</head>
<body>

  <section class="card card-front" aria-label="Card front">
    <div class="brand-lockup">
      <span class="brand-dot"></span>
      <div class="brand-name">
        <span class="line-main">TALVEX</span>
        <span class="line-sub">INDUSTRIAL MAINTENANCE</span>
      </div>
    </div>
  </section>

  <section class="card card-back" aria-label="Card back">
    <svg class="backdrop" width="560" height="320" viewBox="0 0 560 320">
      <defs>
        <linearGradient id="plantTone" x1="0" y1="0" x2="1" y2="0.4">
          <stop offset="0" stop-color="var(--photo-deep)"/>
          <stop offset="0.55" stop-color="var(--photo-mid)"/>
          <stop offset="0.85" stop-color="var(--photo-light)"/>
          <stop offset="1" stop-color="var(--photo-mid)"/>
        </linearGradient>
      </defs>
      <rect width="560" height="320" fill="url(#plantTone)" role="img" aria-label="Photo of an industrial plant interior in blue tones"/>
      <polygon points="0,0 560,0 560,80 470,150 300,150 0,150" fill="var(--card-black)"/>
      <polygon points="0,0 300,0 300,150 0,150" fill="var(--card-black)"/>
      <path d="M0,110 L170,110 L300,150 L0,150 Z" fill="var(--photo-deep)" opacity="0.6"/>
      <path d="M280,320 Q300,230 560,200 L560,320 Z" fill="var(--white)"/>
      <line x1="300" y1="228" x2="450" y2="210" stroke="var(--brand-blue)" stroke-width="3"/>
    </svg>

    <div class="identity">
      <div class="first-name">DALE</div>
      <div class="last-name">VIRNOW JR.</div>
      <div class="role">OWNER</div>
      <div class="rule"></div>
    </div>

    <div class="contacts">
      <div class="contact-pill phone">
        <span class="contact-icon">
          <svg width="12" height="14" viewBox="0 0 12 14"><rect x="2" y="0.5" width="8" height="13" rx="1.5" fill="none" stroke="#fff" stroke-width="1.4"/><circle cx="6" cy="11" r="0.9" fill="#fff"/></svg>
        </span>
        413-627-8154
      </div>
      <div class="contact-pill email">
        <span class="contact-icon">
          <svg width="14" height="10" viewBox="0 0 14 10"><rect x="0.7" y="0.7" width="12.6" height="8.6" rx="1" fill="none" stroke="#fff" stroke-width="1.4"/><polyline points="1,1 7,5.5 13,1" fill="none" stroke="#fff" stroke-width="1.4"/></svg>
        </span>
        dale.virnow.jr@brindlemail.net
      </div>
    </div>

    <div class="corner-brand">
      <span class="brand-dot"></span>
      <span class="brand-name">TALVEX</span>
    </div>
  </section>

</body>
</html>
```